Problem Solving Guide- PDF Template

We are looking for an editable PDF template design for our Epoxy Floor Coatings Problem Solving Guide.

Target Market(s)

This guide will be on our website and we will also email it to customers

Industry/Entity Type

Online Shopping

Colors
f78f20
ffffff
5c5c5c
000000

Requirements
Must have
• We are looking for a very modern and clean design. Each page of the guide will address a different issue. There will be 20-25 pages in total for the completed guide, however we just need a template that we can use to create each page so that they look the same. Each page must have our logo, a spot to add a photo of the issue being discussed. Then each page will have the following sections: DESCRIPTION,CAUSE,REPAIR,PREVENTION. At the bottom of each page we would like to direct people to our website for more information. I am attaching the current guide that we have. This shows the basic information that each page will have but as you can see it is old, outdated and anything but modern. As part of the design you can put the different parts of information in circles, squares, use arrows etc. to make it appealing. I am also attaching a copy of our color chart that appears on our website to give you an idea of some of the other graphic designs that we use. Our colors are Orange (please use the same orange as in our logo) grey, black and white. Our website is www.resinmarko.com. There is also a picture of "bubbles in epoxy"-this is an example of a picture we will show to address one issue.

```html
<!DOCTYPE html>
<html lang="en">
<head>
<meta charset="utf-8">
<title>Resinmarko – Problem Solving Guide Page</title>
<link href="https://fonts.googleapis.com/css2?family=Bebas+Neue&family=Oswald:wght@300;500&family=Montserrat:wght@400;600;700;800&display=swap" rel="stylesheet">
<style>
  :root{
    --orange:#f78f20;
    --orange-deep:#f0682a;
    --grey:#5c5c5c;
    --grey-mid:#7a7a7a;
    --light:#f1f1f1;
    --white:#ffffff;
    --black:#000000;
    --text:#3a3a3a;
  }
  *{margin:0;padding:0;box-sizing:border-box}
  html,body{width:1155px;height:1200px;overflow:hidden;background:var(--white)}
  .page{position:relative;width:1155px;height:1200px;overflow:hidden;font-family:"Montserrat",sans-serif;color:var(--text)}
  .shapes{position:absolute;inset:0}
  .brand{position:absolute;left:0;right:0;top:34px;display:flex;flex-direction:column;align-items:center;gap:10px}
  .brand-row{display:flex;align-items:center;gap:16px}
  .brand-mark{width:26px;height:26px;background:var(--orange-deep)}
  .brand-name{font-weight:700;font-size:44px;line-height:1;color:var(--grey);letter-spacing:6px;text-transform:uppercase}
  .brand-tagline{font-size:15px;font-weight:600;color:var(--grey);letter-spacing:3px;text-transform:uppercase}
  .headline{position:absolute;left:36px;top:468px;font-family:"Bebas Neue",sans-serif;font-size:92px;line-height:1;color:var(--white);letter-spacing:4px}
  .subline{position:absolute;left:38px;top:570px;font-family:"Oswald",sans-serif;font-weight:300;font-size:30px;line-height:1.08;color:var(--white);text-transform:uppercase;letter-spacing:1.5px}
  .subline strong{font-weight:500}
  .subline .small{font-size:24px;letter-spacing:.5px}
  .section{position:absolute;width:490px}
  .section h2{font-weight:800;font-size:27px;line-height:33px;color:var(--orange-deep);letter-spacing:.5px}
  .section h2::after{content:"";display:block;width:48px;height:2px;background:var(--grey);margin:10px 0 14px}
  .section p{font-size:18px;line-height:24px;text-align:justify;color:var(--text)}
  .s-description{left:40px;top:680px}
  .s-cause{left:578px;top:680px;width:500px}
  .s-repair{left:40px;top:895px}
  .s-prevention{left:578px;top:895px;width:500px}
  .phone{position:absolute;left:52px;top:1128px;display:flex;align-items:center;gap:14px;font-weight:800;font-size:46px;line-height:1;color:var(--white);letter-spacing:2px}
  .website{position:absolute;right:32px;top:1168px;font-size:17px;line-height:1;font-weight:600;letter-spacing:4px;color:var(--white)}
</style>
</head>
<body>
<div class="page">
  <svg class="shapes" width="1155" height="1200" viewBox="0 0 1155 1200">
    <defs>
      <linearGradient id="headerBg" x1="0" y1="0" x2="0" y2="1">
        <stop offset="0" stop-color="#ffffff"/><stop offset="1" stop-color="#dcdcdc"/>
      </linearGradient>
      <linearGradient id="orangeBand" x1="0" y1="0" x2="1" y2="0">
        <stop offset="0" stop-color="#f0682a"/><stop offset=".5" stop-color="#f78f20"/><stop offset="1" stop-color="#f0682a"/>
      </linearGradient>
      <linearGradient id="greyBand" x1="0" y1="0" x2="1" y2="0">
        <stop offset="0" stop-color="#5c5c5c"/><stop offset="1" stop-color="#8a8a8a"/>
      </linearGradient>
      <linearGradient id="photoTone" x1="0" y1="0" x2="1" y2="1">
        <stop offset="0" stop-color="#b8862a"/><stop offset=".25" stop-color="#8a2a2a"/>
        <stop offset=".5" stop-color="#3d5fd0"/><stop offset=".75" stop-color="#2fb08a"/>
        <stop offset="1" stop-color="#c9a23a"/>
      </linearGradient>
    </defs>

    <rect x="0" y="0" width="1155" height="190" fill="url(#headerBg)"/>
    <polygon points="0,0 110,0 245,100 0,100" fill="var(--grey)"/>
    <polygon points="1040,0 1155,0 1155,100 910,100" fill="var(--grey)"/>
    <polygon points="0,113 225,113 330,160 825,160 920,113 1155,113 1155,190 0,190" fill="url(#orangeBand)"/>
    <polyline points="0,122 225,122 290,175 520,175" fill="none" stroke="#fff" stroke-width="1.5" opacity=".8"/>
    <polyline points="1155,122 930,122 865,175 635,175" fill="none" stroke="#fff" stroke-width="1.5" opacity=".8"/>
    <circle cx="520" cy="175" r="5" fill="#fff"/><circle cx="635" cy="175" r="5" fill="#fff"/>

    <rect x="0" y="190" width="1155" height="420" fill="url(#photoTone)" role="img" aria-label="Photo of the issue being discussed, such as jars of coloured epoxy pigment"/>

    <polygon points="0,600 880,600 1120,405 1155,405 1155,1200 0,1200" fill="var(--light)"/>
    <polyline points="1155,420 1125,420 1000,545 880,545" fill="none" stroke="#fff" stroke-width="10"/>
    <polyline points="1155,440 1130,440 1010,560 880,560" fill="none" stroke="var(--grey)" stroke-width="5"/>

    <polygon points="0,455 815,455 735,565 650,565 590,640 0,640" fill="url(#greyBand)"/>
    <polygon points="770,510 805,510 765,565 730,565" fill="var(--orange-deep)"/>
    <polygon points="820,510 855,510 815,565 780,565" fill="var(--grey-mid)"/>
    <polygon points="870,510 905,510 865,565 830,565" fill="var(--orange-deep)"/>
    <polyline points="0,648 525,648 598,582 728,582" fill="none" stroke="var(--orange-deep)" stroke-width="2"/>
    <circle cx="728" cy="582" r="6" fill="var(--orange-deep)"/>

    <polygon points="95,1078 1155,1078 1155,1138 762,1138 725,1102 115,1102" fill="url(#greyBand)"/>
    <polygon points="0,1035 72,1108 700,1108 790,1200 0,1200" fill="url(#orangeBand)"/>
    <polygon points="742,1158 1155,1158 1155,1200 784,1200" fill="#1c1c1c"/>
  </svg>

  <header class="brand">
    <div class="brand-row">
      <div class="brand-mark"></div>
      <div class="brand-name">resinmarko</div>
    </div>
    <div class="brand-tagline">Floor Coatings Problem Solving Guide</div>
  </header>

  <h1 class="headline">HEADLINE GOES HERE</h1>
  <p class="subline">Learn more about what<br><span class="small"><strong>RESINMARKO.COM</strong> can do for you.</span></p>

  <section class="section s-description">
    <h2>DESCRIPTION</h2>
    <p>Lorem Ipsum is simply dummy text of the printing and typesetting industry. Lorem Ipsum has been the industry's standard dummy text ever since the 1500s, when an unknown printer took a galley of type and scrambled it to make a type specimen book.</p>
  </section>
  <section class="section s-cause">
    <h2>CAUSE</h2>
    <p>Lorem Ipsum is simply dummy text of the printing and typesetting industry. Lorem Ipsum has been the industry's standard dummy text ever since the 1500s, when an unknown printer took a galley of type and scrambled it to make a type specimen book.</p>
  </section>
  <section class="section s-repair">
    <h2>REPAIR</h2>
    <p>Lorem Ipsum is simply dummy text of the printing and typesetting industry. Lorem Ipsum has been the industry's standard dummy text ever since the 1500s, when an unknown printer took.</p>
  </section>
  <section class="section s-prevention">
    <h2>PREVENTION</h2>
    <p>Lorem Ipsum is simply dummy text of the printing and typesetting industry. Lorem Ipsum has been the industry's standard dummy text ever since the 1500s, when an unknown printer took a galley.</p>
  </section>

  <footer>
    <div class="phone">
      <svg width="36" height="36" viewBox="0 0 24 24" aria-hidden="true"><path fill="#fff" d="M6.6 10.8a15.1 15.1 0 0 0 6.6 6.6l2.2-2.2c.3-.3.7-.4 1-.2 1.1.4 2.3.6 3.6.6.6 0 1 .4 1 1V20c0 .6-.4 1-1 1A17 17 0 0 1 3 4c0-.6.4-1 1-1h3.5c.6 0 1 .4 1 1 0 1.3.2 2.5.6 3.6.1.3 0 .7-.2 1z"/><path fill="none" stroke="#fff" stroke-width="1.8" d="M14 3.5a7 7 0 0 1 6.5 6.5M14 7a3.5 3.5 0 0 1 3 3"/></svg>
      <span>1-(888) 555-0147</span>
    </div>
    <div class="website">www.resinmarko.com</div>
  </footer>
</div>
</body>
</html>
```